Coralbend Pastoral Traders Business Cards

We require business cards revamped with our logo. A few details we would like to use.

1. Round Edges
2. Our logo over the top of a wagyu cattle background photo on one side of the card

Other side of the card has the below details.

1. Person Name (First & Last)
2. Job Position
3. Mobile Number
4. Email Address
5. Website Address

Simple & Neat.

Target Market(s)

Sales

Industry/Entity Type

Agriculture

Contact Information for Business Card

CORALBEND PASTORAL TRADERS

Colors

Designer to choose colors to be used in the design.

Requirements
Must have
• Company Logo

```html
<!DOCTYPE html>
<html lang="en">
<head>
<meta charset="utf-8">
<title>Coralbend Pastoral Traders – Business Cards</title>
<link rel="stylesheet" href="https://fonts.googleapis.com/css2?family=Cinzel:wght@600;700&family=Montserrat:wght@400;500&display=swap">
<style>
  :root {
    --bg: #ece8e3;
    --brand-red: #7a1218;
    --brand-maroon: #5c0d1d;
    --card-white: #ffffff;
    --card-grey: #e4e4e4;
    --ink-red: #6e1420;
    --ink-grey: #4a4a4a;
  }
  * { box-sizing: border-box; margin: 0; padding: 0; }
  html, body {
    width: 1200px; height: 900px; overflow: hidden;
    background: var(--bg);
  }
  .canvas { position: relative; width: 1200px; height: 900px; }

  .card {
    position: absolute;
    width: 640px; height: 380px;
    border-radius: 44px;
    border: 9px solid var(--brand-maroon);
    overflow: hidden;
  }
  .card--front {
    left: 60px; top: 55px;
    background: var(--brand-red);
    display: flex; align-items: center; justify-content: center;
  }
  .card--back {
    left: 500px; top: 465px;
    background: linear-gradient(120deg, var(--card-grey) 0%, var(--card-white) 55%, var(--card-white) 100%);
    display: flex; flex-direction: column; align-items: center;
    padding-top: 52px;
  }

  .brand { display: flex; align-items: center; gap: 16px; }
  .brand__dot {
    width: 54px; height: 54px; border-radius: 50%;
    border: 6px solid currentColor; flex: none;
  }
  .brand__name {
    font-family: "Cinzel", serif; font-weight: 700;
    line-height: 1.05; text-align: left;
  }
  .brand__main { display: block; font-size: 46px; letter-spacing: 1px; }
  .brand__sub { display: block; font-size: 19px; letter-spacing: 6px; }
  .card--front .brand { color: var(--card-white); }
  .card--back .brand { color: var(--ink-red); }
  .card--back .brand__main { font-size: 40px; }
  .card--back .brand__sub { font-size: 17px; letter-spacing: 5px; }

  .person {
    margin-top: 34px;
    display: flex; align-items: center; gap: 14px;
    width: 460px;
  }
  .person__rule { flex: 1; height: 2px; background: var(--ink-red); }
  .person__name {
    font-family: "Cinzel", serif; font-weight: 700;
    font-size: 21px; color: var(--ink-red); letter-spacing: 1px;
  }
  .person__role {
    font-family: "Montserrat", sans-serif; font-weight: 400;
    font-size: 16px; color: var(--ink-grey); margin-top: 4px;
  }

  .contacts { list-style: none; margin-top: 22px; }
  .contacts__item {
    display: flex; align-items: center; gap: 10px;
    font-family: "Montserrat", sans-serif; font-size: 16px;
    color: var(--ink-grey); margin-bottom: 8px;
  }
  .contacts__icon { width: 18px; height: 18px; flex: none; }
</style>
</head>
<body>
<main class="canvas">

  <section class="card card--front" aria-label="Card front">
    <div class="brand">
      <span class="brand__dot"></span>
      <span class="brand__name">
        <span class="brand__main">CORALBEND</span>
        <span class="brand__sub">PASTORAL TRADERS</span>
      </span>
    </div>
  </section>

  <section class="card card--back" aria-label="Card back">
    <div class="brand">
      <span class="brand__dot"></span>
      <span class="brand__name">
        <span class="brand__main">CORALBEND</span>
        <span class="brand__sub">PASTORAL TRADERS</span>
      </span>
    </div>

    <div class="person">
      <span class="person__rule"></span>
      <span class="person__name">MARCUS HALLOWAY</span>
      <span class="person__rule"></span>
    </div>
    <p class="person__role">Director</p>

    <ul class="contacts">
      <li class="contacts__item">
        <svg class="contacts__icon" viewBox="0 0 18 18" aria-hidden="true">
          <rect x="5" y="1.5" width="8" height="15" rx="1.5" fill="none" stroke="#6e1420" stroke-width="1.6"/>
          <line x1="8" y1="14" x2="10" y2="14" stroke="#6e1420" stroke-width="1.4"/>
        </svg>
        417-382-0594
      </li>
      <li class="contacts__item">
        <svg class="contacts__icon" viewBox="0 0 18 18" aria-hidden="true">
          <rect x="1.5" y="4" width="15" height="10" fill="#6e1420"/>
          <polyline points="1.5,4 9,10 16.5,4" fill="none" stroke="#fff" stroke-width="1.3"/>
        </svg>
        info@coralbendpastoral.com
      </li>
      <li class="contacts__item">
        <svg class="contacts__icon" viewBox="0 0 18 18" aria-hidden="true">
          <circle cx="9" cy="9" r="7.5" fill="none" stroke="#6e1420" stroke-width="1.4"/>
          <ellipse cx="9" cy="9" rx="3.4" ry="7.5" fill="none" stroke="#6e1420" stroke-width="1.2"/>
          <line x1="1.5" y1="9" x2="16.5" y2="9" stroke="#6e1420" stroke-width="1.2"/>
        </svg>
        www.coralbendpastoral.com
      </li>
    </ul>
  </section>

</main>
</body>
</html>
```